IT Company Business Card Rebranding

We want to modernize our business cards massively. We want to incorporate aspects of our old business card such as the white and geometric design with the blues of another icon. Existing Logo, old business card and icon are all attached.

We are a modern IT company that provides support for new and growing technologies and want our business cards to be modern yet professional.
Updates

Note: Do not use file ICON.png in design. This is just a design we like Added Wednesday, March 9, 2016

Industry/Entity Type

Information Technology

Contact Information for Business Card

Roughly 43 : 26 or 1075 x 650 px

Font styles to use
Serif

Colors
0492cd
3276b5
33a6d7
86cfc6
cfeae6
cee9f5
ffffff

Requirements
Must have
• Modern yet professional
Nice to have
• We would like to incorporate the blues of our existing logo and of the icon provided. Really like the design of the icon.
Should not have
• Too Decorative. Just simple and professional.
• Not have the circle icon, as it is a copyrighted icon, I just like the colors and the geometric design

```html
<!DOCTYPE html>
<html lang="en">
<head>
<meta charset="utf-8">
<title>Brightlane – Business Card</title>
<link rel="stylesheet" href="https://fonts.googleapis.com/css2?family=Open+Sans:wght@400;600;700&display=swap">
<style>
  :root {
    --page-bg: #eef1f5;
    --card-white: #ffffff;
    --blue-deep: #2444a8;
    --blue-mid: #3276b5;
    --blue-bright: #3a7fd0;
    --blue-light: #33a6d7;
    --blue-sky: #4fb3ee;
    --text-grey: #6d7480;
    --text-white: #ffffff;
  }
  html, body {
    margin: 0;
    padding: 0;
    width: 1200px;
    height: 900px;
    overflow: hidden;
    background: var(--page-bg);
    font-family: "Open Sans", Arial, sans-serif;
  }
  .canvas { position: relative; width: 1200px; height: 900px; }
  .card {
    position: absolute;
    width: 556px;
    height: 343px;
    overflow: hidden;
    box-shadow: 0 6px 18px rgba(20, 40, 80, 0.18);
  }
  .card-front { left: 238px; top: 62px; background: var(--card-white); }
  .card-back {
    left: 458px; top: 518px;
    background: linear-gradient(180deg, var(--blue-bright) 0%, #3f78cf 50%, #3461d2 100%);
  }
  .card svg { position: absolute; inset: 0; }
  .brand-name {
    position: absolute;
    margin: 0;
    font-weight: 400;
    white-space: nowrap;
    letter-spacing: 1px;
  }
  .card-front .brand-name {
    left: 54px; top: 118px;
    font-size: 24px;
    color: var(--text-grey);
  }
  .card-back .brand-name {
    left: 0; right: 0; top: 150px;
    text-align: center;
    font-size: 36px;
    color: var(--text-white);
  }
  .holder {
    position: absolute;
    left: 50px; top: 266px;
    color: var(--text-white);
  }
  .holder-name { margin: 0; font-size: 20px; font-weight: 700; line-height: 24px; }
  .holder-role { margin: 0; font-size: 14.5px; line-height: 20px; }
  .contact-list {
    position: absolute;
    right: 38px; top: 248px;
    margin: 0; padding: 0;
    list-style: none;
    color: var(--text-white);
    font-size: 14.5px;
    text-align: right;
  }
  .contact-list li {
    display: flex;
    justify-content: flex-end;
    align-items: center;
    gap: 10px;
    height: 20px;
  }
  .contact-list svg { position: static; width: 12px; height: 12px; }
  .pattern-band { position: absolute; left: 0; right: 0; }
  .front-pattern {
    bottom: 0; height: 95px;
    background: linear-gradient(180deg, rgba(58,127,208,0) 0%, rgba(52,100,214,0.55) 100%);
  }
  .back-pattern-top {
    top: 0; height: 92px;
    background: linear-gradient(180deg, var(--blue-sky) 0%, rgba(58,127,208,0) 100%);
  }
  .back-pattern-bottom {
    bottom: 0; height: 92px;
    background: linear-gradient(180deg, rgba(52,97,210,0) 0%, #2f55c8 100%);
  }
</style>
</head>
<body>
<main class="canvas">

  <section class="card card-front" aria-label="Business card front">
    <svg width="556" height="343" viewBox="0 0 556 343" aria-hidden="true">
      <defs>
        <linearGradient id="front-blue" x1="0" y1="0" x2="0" y2="1">
          <stop offset="0" stop-color="#2f5bbd"/>
          <stop offset="0.45" stop-color="#3b7ed0"/>
          <stop offset="1" stop-color="#3a72d6"/>
        </linearGradient>
      </defs>
      <path d="M0,140 C70,235 300,250 556,110 L556,343 L0,343 Z" fill="url(#front-blue)"/>
      <path d="M0,140 C70,235 300,250 556,110 L556,143 C320,250 80,245 0,170 Z" fill="var(--blue-deep)"/>
      <path d="M0,172 C90,252 320,252 556,146" fill="none" stroke="#ffffff" stroke-width="4"/>
    </svg>

    <div class="pattern-band front-pattern" role="img" aria-label="Faceted geometric blue pattern along the lower edge"></div>

    <p class="brand-name">Brightlane</p>

    <div class="holder">
      <p class="holder-name">MILO</p>
      <p class="holder-role">technical services</p>
    </div>

    <ul class="contact-list">
      <li>055-210 384 617
        <svg viewBox="0 0 12 12" aria-hidden="true"><path d="M2.5,1 L4.5,1 L5.3,3.6 L4,4.5 C4.6,6 6,7.4 7.5,8 L8.4,6.7 L11,7.5 L11,9.5 C11,10.4 10.3,11 9.5,11 C5,11 1,7 1,2.5 C1,1.7 1.6,1 2.5,1 Z" fill="#ffffff"/></svg>
      </li>
      <li>info@brightlane.com
        <svg viewBox="0 0 12 12" aria-hidden="true"><rect x="1" y="2.5" width="10" height="7" fill="#ffffff"/><path d="M1,2.5 L6,6.5 L11,2.5" fill="none" stroke="#3a72d6" stroke-width="1"/></svg>
      </li>
      <li>www.brightlane.com
        <svg viewBox="0 0 12 12" aria-hidden="true"><circle cx="6" cy="6" r="5" fill="#ffffff"/><path d="M1,6 H11 M6,1 C3.5,3.5 3.5,8.5 6,11 M6,1 C8.5,3.5 8.5,8.5 6,11" fill="none" stroke="#3a72d6" stroke-width="0.8"/></svg>
      </li>
    </ul>
  </section>

  <section class="card card-back" aria-label="Business card back">
    <div class="pattern-band back-pattern-top" role="img" aria-label="Faceted geometric light blue pattern along the top edge"></div>
    <p class="brand-name">Brightlane</p>
    <div class="pattern-band back-pattern-bottom" role="img" aria-label="Faceted geometric deep blue pattern along the bottom edge"></div>
  </section>

</main>
</body>
</html>
```